Oven Cleaning Business owner needs business card design

Hi there,
Would like for a business card to be designed for myself, the owner of a professional oven cleaning business on the Sunshine Coast.
Would like it to look sleek, and modern-ish. Bit creative is encouraged too.
Include following:
Name/title: Corin ter Haghe, Owner
Phone number: 1300 482 916
Email: info@hearthshinecrew.com.au
Website: www.hearthshinecrew.com.au

```html
<!DOCTYPE html>
<html lang="en">
<head>
<meta charset="utf-8">
<title>Hearthshine Crew – Business Card</title>
<link href="https://fonts.googleapis.com/css2?family=Open+Sans:wght@400;600&family=Archivo+Black&display=swap" rel="stylesheet">
<style>
  :root {
    --backdrop: #d9d9d7;
    --paper: #f9f8f5;
    --paper-white: #ffffff;
    --charcoal: #2c2f30;
    --teal: #1cdddb;
    --rail-grey: #929698;
    --text-light: #dcdcdc;
    --ink: #111111;
  }
  * { box-sizing: border-box; margin: 0; padding: 0; }
  html, body { width: 1200px; height: 1200px; overflow: hidden; }
  body {
    background: var(--backdrop);
    position: relative;
    font-family: "Open Sans", Arial, sans-serif;
  }
  .card {
    position: absolute;
    left: 183px;
    width: 834px;
    height: 476px;
    overflow: hidden;
    box-shadow: 14px 16px 18px rgba(0,0,0,0.35);
  }
  .card-front { top: 75px; background: var(--paper); }
  .card-back { top: 649px; background: var(--charcoal); }

  /* brand lockup */
  .brand {
    position: absolute;
    display: flex;
    flex-direction: column;
    align-items: center;
    gap: 18px;
    transform: translateX(-50%);
    z-index: 1;
  }
  .brand-mark {
    width: 118px; height: 118px;
    border-radius: 50%;
    background: var(--teal);
  }
  .brand-name {
    font-family: "Archivo Black", Arial, sans-serif;
    color: var(--teal);
    font-size: 20px;
    letter-spacing: 1px;
    white-space: nowrap;
  }
  .card-front .brand { left: 417px; top: 95px; }
  .card-back .brand { left: 167px; top: 130px; }

  /* front */
  .front-band {
    position: absolute; left: 0; right: 0; top: 408px; bottom: 0;
    background: var(--charcoal);
  }
  .front-stripe { position: absolute; left: 0; top: 0; width: 834px; height: 476px; }
  .web-pill {
    position: absolute; left: 247px; top: 386px;
    width: 340px; height: 45px;
    border-radius: 22px;
    background: var(--teal);
    color: var(--paper-white);
    font-weight: 600;
    font-size: 19px;
    display: flex; align-items: center; justify-content: center;
  }

  /* back */
  .back-panel {
    position: absolute; left: 0; top: 0; bottom: 0; width: 334px;
    background: var(--paper-white);
  }
  .back-divider {
    position: absolute; left: 344px; top: 0; bottom: 0; width: 5px;
    background: var(--paper-white);
  }
  .icon-rail {
    position: absolute; left: 400px; top: 58px;
    width: 47px; height: 365px;
    border-radius: 16px;
    background: var(--rail-grey);
  }
  .icon { position: absolute; left: 404px; width: 40px; height: 40px; }
  .icon-person { top: 104px; }
  .icon-phone { top: 211px; }
  .icon-mail { top: 270px; }
  .icon-web { top: 328px; }
  .rail-rule {
    position: absolute; left: 410px; width: 28px; height: 2px;
    background: #6e7274;
  }
  .holder-name {
    position: absolute; left: 469px; top: 108px;
    color: var(--text-light);
    font-weight: 600; font-size: 33px; white-space: nowrap;
  }
  .holder-title {
    position: absolute; left: 471px; top: 153px;
    color: var(--text-light); font-size: 17px;
  }
  .contact {
    position: absolute; left: 471px;
    color: var(--text-light); font-size: 17px; white-space: nowrap;
  }
  .contact-phone { top: 218px; }
  .contact-mail { top: 286px; left: 474px; }
  .contact-web { top: 343px; left: 468px; }
</style>
</head>
<body>

<section class="card card-front">
  <div class="brand">
    <div class="brand-mark"></div>
    <div class="brand-name">HEARTHSHINE CREW</div>
  </div>
  <div class="front-band"></div>
  <svg class="front-stripe" viewBox="0 0 834 476" aria-hidden="true">
    <polygon points="756,408 787,408 698,476 664,476" fill="var(--paper)"/>
  </svg>
  <div class="web-pill">www.hearthshinecrew.com.au</div>
</section>

<section class="card card-back">
  <div class="back-panel"></div>
  <div class="back-divider"></div>
  <div class="brand">
    <div class="brand-mark"></div>
    <div class="brand-name">HEARTHSHINE CREW</div>
  </div>

  <div class="icon-rail"></div>
  <svg class="icon icon-person" viewBox="0 0 40 40" aria-hidden="true">
    <circle cx="20" cy="12" r="9" fill="var(--teal)"/>
    <path d="M2 38 C4 26 12 22 20 22 C28 22 36 26 38 38 Z" fill="var(--teal)"/>
  </svg>
  <svg class="icon icon-phone" viewBox="0 0 40 40" aria-hidden="true">
    <path d="M8 4 L14 4 L16 12 L12 15 C14 22 18 27 25 30 L28 26 L36 29 L35 35 C33 38 28 38 22 35 C13 30 7 22 5 13 C4 8 5 5 8 4 Z" fill="none" stroke="var(--teal)" stroke-width="3" stroke-linejoin="round"/>
  </svg>
  <div class="rail-rule" style="top:261px"></div>
  <svg class="icon icon-mail" viewBox="0 0 40 40" aria-hidden="true">
    <rect x="3" y="8" width="34" height="24" fill="none" stroke="var(--teal)" stroke-width="3"/>
    <path d="M3 9 L20 23 L37 9" fill="none" stroke="var(--teal)" stroke-width="3"/>
  </svg>
  <div class="rail-rule" style="top:320px"></div>
  <svg class="icon icon-web" viewBox="0 0 40 40" aria-hidden="true">
    <circle cx="18" cy="18" r="15" fill="none" stroke="var(--teal)" stroke-width="3"/>
    <ellipse cx="18" cy="18" rx="6" ry="15" fill="none" stroke="var(--teal)" stroke-width="2.5"/>
    <line x1="3" y1="18" x2="33" y2="18" stroke="var(--teal)" stroke-width="2.5"/>
    <path d="M22 20 L36 28 L30 30 L33 37 L30 38 L27 31 L22 35 Z" fill="#17a8a6"/>
  </svg>

  <div class="holder-name">Corin ter Haghe</div>
  <div class="holder-title">Owner</div>
  <div class="contact contact-phone">1300 482 916</div>
  <div class="contact contact-mail">info@hearthshinecrew.com.au</div>
  <div class="contact contact-web">www.hearthshinecrew.com.au</div>
</section>

</body>
</html>
```